Business Card and Membership Card Design

Hi there.
This is Martin from K-arrow Sports Club. I would like to design a business card for myself. K-arrow Sports Club is a recreational sports club, we do basketball, badminton, table tennis and 8 ball pool. At this moment, I've a club business card and a loyalty card but I need a new format business for myself as a General Manager at the club and also a design for my club membership card. Can you please reply my email and I'll send the detailed description of what I'd like to do?
The email address is martinrowanpell@kelvarmail.com

Target Market(s)

Recreational Sports, Social Sports Activity. Basketball, Indoor Soccer, Badminton Table Tennis.
Group booking, Event Hosting, Holiday Program, Sports Coaching, Kids program. birthday party

Industry/Entity Type

Recreation

Contact Information for Business Card

Name: Ridgeline Rec
Slogan: Play it forward
General Manager: Martin Pell
Contact: 027 5193846
Weichat: martinrowanpell
Company Address: Unit 7, 18 Harwick Street, New Lynn, Auckland.
Email: martinrowanpell@kelvarmail.com
And on the back of the card:
Basketball
Indoor Soccer
Badminton
Table Tennis
Group / Company Booking
Event Hosting
Birthday Party
Holiday Program
Kids Training

Font styles to use
Sans Serif

Requirements
Must have
• My project must have all of the information and clear details.
• I'd like to make the format simple and looks smart.
• As a sports club, I prefer this design looks like positive, power, and moden
Nice to have
• As a sports club, I prefer this design looks like positive, power, and modern
• Probably make this design in a black card and the edge side is around.

```html
<!DOCTYPE html>
<html lang="en">
<head>
<meta charset="utf-8">
<title>Ridgeline Rec – Business Card</title>
<link rel="stylesheet" href="https://fonts.googleapis.com/css2?family=Open+Sans:wght@400;600;700&display=swap">
<style>
  :root {
    --backdrop: #e4e2e0;
    --card: #242122;
    --band: #a9a9a9;
    --accent-block: #5a5a5a;
    --text-light: #f2f2f2;
    --text-soft: #d8d8d8;
    --text-grey: #9a9a9a;
    --rule: #3c393a;
    --white: #ffffff;
  }
  * { margin: 0; padding: 0; box-sizing: border-box; }
  html, body { width: 1200px; height: 844px; overflow: hidden; }
  body {
    background: var(--backdrop);
    position: relative;
    font-family: "Open Sans", Arial, sans-serif;
  }
  .card {
    position: absolute;
    top: 272px;
    width: 520px;
    height: 300px;
    background: var(--card);
    border-radius: 4px;
    overflow: hidden;
    box-shadow: 0 8px 24px rgba(0,0,0,0.25);
  }
  .card--front { left: 50px; }
  .card--back { left: 630px; }

  /* Front */
  .band { position: absolute; left: 0; width: 100%; height: 14px; background: var(--band); }
  .band--top { top: 0; }
  .band--bottom { bottom: 0; }
  .contact {
    position: absolute; left: 0; right: 0; top: 58px;
    text-align: center; color: var(--text-light);
  }
  .contact__name { font-size: 19px; font-weight: 700; color: var(--text-grey); line-height: 1.1; }
  .contact__title { font-size: 14px; color: var(--text-soft); margin-top: 2px; }
  .contact__rule { width: 230px; height: 1px; background: var(--rule); margin: 16px auto; }
  .contact__line { font-size: 15px; line-height: 1.45; }
  .contact__address { font-size: 16px; }

  /* Back */
  .brand {
    position: absolute; left: 0; right: 0; top: 40px; text-align: center;
  }
  .brand__dash { width: 44px; height: 2px; background: var(--white); margin: 0 auto 24px; }
  .brand__name {
    font-family: "Open Sans", Arial, sans-serif;
    font-weight: 600; font-size: 28px; letter-spacing: 1px;
    color: var(--white); line-height: 1.2;
  }
  .services {
    margin-top: 10px; color: var(--text-soft);
    font-size: 13px; line-height: 1.3;
  }
  .services .sep { margin: 0 6px; }
  .services__rule { width: 260px; height: 1px; background: var(--rule); margin: 14px auto 12px; }
  .slogan {
    font-weight: 700; font-size: 16px; color: var(--text-grey);
    text-transform: uppercase; letter-spacing: 0.3px;
  }
  .accent { position: absolute; width: 24px; height: 46px; background: var(--accent-block); }
  .accent-line { position: absolute; width: 3px; height: 46px; background: var(--white); }
  .accent--right { right: 0; top: 40px; }
  .accent-line--right { right: 34px; top: 40px; }
  .accent--left { left: 0; top: 214px; }
  .accent-line--left { left: 34px; top: 214px; }
</style>
</head>
<body>
  <section class="card card--front" aria-label="Business card front">
    <div class="band band--top"></div>
    <div class="contact">
      <p class="contact__name">Martin Pell</p>
      <p class="contact__title">General Manager</p>
      <div class="contact__rule"></div>
      <p class="contact__line">027 5193846</p>
      <p class="contact__line">martinrowanpell@kelvarmail.com</p>
      <div class="contact__rule"></div>
      <p class="contact__line contact__address">Unit 7, 18 Harwick Street, New Lynn, AKL.</p>
    </div>
    <div class="band band--bottom"></div>
  </section>

  <section class="card card--back" aria-label="Business card back">
    <div class="accent accent--right"></div>
    <div class="accent-line accent-line--right"></div>
    <div class="accent accent--left"></div>
    <div class="accent-line accent-line--left"></div>
    <div class="brand">
      <div class="brand__dash"></div>
      <h1 class="brand__name">Ridgeline Rec</h1>
      <div class="services">
        <p>Basketball<span class="sep">|</span>Indoor Soccer<span class="sep">|</span>Badminton</p>
        <p>Table Tennis<span class="sep">|</span>Group / Company Booking</p>
        <p>Event Hosting<span class="sep">|</span>Birthday Party</p>
        <p>Holiday Program<span class="sep">|</span>Kids Training</p>
      </div>
      <div class="services__rule"></div>
      <p class="slogan">Play it forward</p>
    </div>
  </section>
</body>
</html>
```